Water Bottle Design

We are launching a water bottle and need a impactful design.

Target Market(s)

health conscious hipsters

Font styles to use
Sans Serif

Requirements
Must have
• Please include the logo (included) on one side of the bottle and these words on the other side of the bottle. "It’s simple, REUSE this bottle every day. Your action, will REDUCE the amount of waste produced. SAVE your body from drinking the harmful contaminants in your water from Non-BPA plastics. HELP someone else because proceeds from your purchase will help homeless veterans.
• We’re just two dudes that like to drink water and help people. #Driftwell"
• Use a total of two colors
• UPDATE: You do not have to use the bottle on the logo.
Nice to have
• The bottle itself is 34 ounces and looks like a normal water bottle. I will include the image in the files. We would need to be able to change the colors easily.
Should not have
• Do not use more than two colors. Colors should not be important to the design at this point.

```html
<!DOCTYPE html>
<html lang="en">
<head>
<meta charset="utf-8">
<title>Driftwell Bottle Label</title>
<link rel="stylesheet" href="https://fonts.googleapis.com/css2?family=Open+Sans:wdth,wght@75..100,300..700&display=swap">
<style>
  :root {
    --sky: #cfeaf8;
    --waterline: #3c9fdd;
    --water: #62c2ec;
    --brand-blue: #1e8fd8;
    --ice-light: #eef7fc;
    --ice-mid: #a9d2ec;
    --ice-deep: #3e8fcf;
    --ice-base: #3576b8;
    --ink: #1d1d1d;
    --white: #ffffff;
  }
  * { margin: 0; padding: 0; box-sizing: border-box; }
  html, body { width: 1200px; height: 368px; overflow: hidden; background: var(--white); }
  .label {
    position: relative;
    width: 1200px;
    height: 368px;
    overflow: hidden;
    background: var(--water);
    font-family: "Open Sans", Arial, sans-serif;
  }
  .label__sky {
    position: absolute; left: 0; top: 0;
    width: 100%; height: 182px;
    background: var(--sky);
  }
  .label__waterline {
    position: absolute; left: 0; top: 182px;
    width: 100%; height: 8px;
    background: var(--waterline);
  }
  .iceberg {
    position: absolute;
    border-radius: 46% 46% 28% 28%;
  }
  .iceberg--main {
    left: 392px; top: 2px; width: 258px; height: 356px;
    background: linear-gradient(180deg, var(--ice-light) 0%, var(--ice-mid) 50%, var(--ice-deep) 52%, var(--ice-base) 100%);
  }
  .iceberg--faint {
    left: 960px; top: 24px; width: 240px; height: 344px;
    opacity: 0.4;
    background: linear-gradient(180deg, var(--ice-light) 0%, var(--ice-mid) 46%, var(--ice-deep) 52%, var(--water) 100%);
  }
  .brand-mark {
    position: absolute; left: 190px; top: 90px;
    display: flex; align-items: center; gap: 10px;
  }
  .brand-mark__square {
    width: 20px; height: 20px;
    background: var(--brand-blue);
  }
  .brand-mark__name {
    font-weight: 600;
    font-size: 28px;
    line-height: 1;
    color: var(--brand-blue);
  }
  .brand-wordmark {
    position: absolute; left: 103px; top: 208px;
    font-weight: 400;
    font-size: 34px;
    line-height: 1.2;
    color: var(--white);
  }
  .message {
    position: absolute; left: 695px; top: 28px;
    width: 395px;
    font-size: 14.5px;
    font-stretch: 85%;
    line-height: 20px;
    color: var(--ink);
    text-align: justify;
  }
  .hashtag {
    position: absolute; left: 960px; top: 146px;
    font-weight: 600;
    font-size: 24px;
    line-height: 1.2;
    color: var(--ink);
  }
  .price-panel {
    position: absolute; left: 701px; top: 247px;
    width: 385px; height: 102px;
    background: var(--white);
    border-radius: 18px;
    padding: 24px 0 0 26px;
  }
  .price-panel__text {
    font-size: 10px;
    color: var(--ink);
  }
</style>
</head>
<body>
  <div class="label">
    <div class="label__sky"></div>
    <div class="label__waterline"></div>

    <div class="iceberg iceberg--main" role="img" aria-label="Iceberg illustration, white peak above the waterline and blue mass below"></div>
    <div class="iceberg iceberg--faint" role="img" aria-label="Faint second iceberg in the background"></div>

    <div class="brand-mark">
      <span class="brand-mark__square"></span>
      <span class="brand-mark__name">Driftwell</span>
    </div>

    <div class="brand-wordmark">Driftwell</div>

    <p class="message">It’s simple, REUSE this bottle every day. Your action, will REDUCE the amount of waste produced. SAVE your body from drinking the harmful contaminants in your water from Non-BPA plastics. HELP someone else because proceeds from your purchase will help homeless veterans.</p>

    <div class="hashtag">#Driftwell</div>

    <div class="price-panel">
      <p class="price-panel__text">Prices &amp; Stuff ....................</p>
    </div>
  </div>
</body>
</html>
```